Need a FLYER/BROCHURE for selling woman hair. I have an online business and need your help.

I need a flyer/BROCHURE that represents my company. We sale hair online and needing for our customers to know our prices and discounts for any holiday and upcoming new year specials. I need the brochure to stand out. Have our brand Logo on it. Pictures of hair we sale on our site and models on the flyer. Prices will need to be place on the flyer indicating before and after the discounts. I also have a bag gift for loyal customers that need to be on the flyer. Colors I am interested in are purple and Gold. Or something creative that will blend with my logo. On my prices I sent. I need to change the title Best, Medium and Low Quality to 6A, 5A, to The Calder Range.

Reason: I would like the deadline to change. The reason I see some designers are coming to my project and some are saying the deadline is too short. I would like to see what they can offer me before I decide.

Industry/Entity Type

Business

Requirements
Must have
• Pictures of my brand. Prices that matches my original prices and sales prices. Pictures of hair and models.

```html
<!DOCTYPE html>
<html lang="en">
<head>
<meta charset="utf-8">
<title>The Calder Range — Price List</title>
<link rel="stylesheet" href="https://fonts.googleapis.com/css2?family=Cinzel:wght@700&family=Comfortaa:wght@600&family=Questrial&display=swap">
<style>
  :root {
    --ink-black: #0b0a0b;
    --plum: #6d1140;
    --plum-card: #8a1b55;
    --gold: #e6bd55;
    --gold-deep: #b98a2c;
    --card-text: #f6dfea;
    --hair-dark: #1b2333;
    --hair-mid: #3b4a63;
    --blossom: #d23a7c;
    --skin: #c98f78;
  }
  * { margin: 0; padding: 0; box-sizing: border-box; }
  html, body { width: 854px; height: 1200px; overflow: hidden; background: var(--plum); }
  .flyer { position: relative; width: 854px; height: 1200px; overflow: hidden; background: var(--plum); font-family: "Questrial", sans-serif; }
  .backdrop { position: absolute; inset: 0; }

  .brand { position: absolute; top: 74px; left: 0; width: 854px; text-align: center; }
  .brand-dot { display: block; width: 54px; height: 54px; margin: 0 auto 12px; border-radius: 50%; background: var(--gold); }
  .brand-name { font-family: "Cinzel", serif; font-weight: 700; font-size: 27px; letter-spacing: 2px; color: var(--gold); }

  .title { position: absolute; left: 258px; top: 270px; font-family: "Cinzel", serif; font-weight: 700; font-size: 64px; line-height: 68px; color: var(--gold); text-shadow: 0 3px 4px rgba(0,0,0,.45); }
  .offer { position: absolute; left: 531px; font-family: "Comfortaa", sans-serif; font-weight: 600; color: var(--gold); text-shadow: 0 2px 3px rgba(0,0,0,.35); }
  .offer-discounts { top: 252px; font-size: 49px; line-height: 64px; letter-spacing: 1px; }
  .offer-gift { top: 432px; font-size: 37px; left: 528px; }
  .offer-loyal { top: 482px; font-size: 24px; left: 507px; }

  .price-card { position: absolute; background: var(--plum-card); color: var(--card-text); font-size: 16px; padding: 10px 14px 0 17px; }
  .price-card h3 { font-weight: 400; font-size: 16px; line-height: 21px; }
  .price-card .unit { line-height: 22px; margin-bottom: 4px; }
  .price-card table { border-collapse: collapse; }
  .price-card td { line-height: 22px; padding: 0; }
  .price-card td:first-child { width: 77px; }
  .price-card.indented table, .price-card.indented .unit { margin-left: 20px; }

  .card-high { left: 44px; top: 550px; width: 141px; height: 274px; }
  .card-medium { left: 217px; top: 553px; width: 151px; height: 395px; }
  .card-low { left: 389px; top: 553px; width: 151px; height: 281px; }
  .card-ombre { left: 571px; top: 553px; width: 235px; height: 235px; }
  .card-best-lace { left: 44px; top: 972px; width: 173px; height: 240px; }
  .card-cheap-lace { left: 229px; top: 972px; width: 171px; height: 240px; }
  .card-solid { left: 412px; top: 972px; width: 235px; height: 240px; }
  .card-deep { left: 659px; top: 972px; width: 200px; height: 240px; }

  .photo-round { position: absolute; left: 33px; top: 823px; width: 145px; height: 145px; border-radius: 50%; background: radial-gradient(circle at 60% 40%, var(--hair-mid), var(--hair-dark) 70%); }
  .photo-oval { position: absolute; left: 524px; top: 799px; width: 340px; height: 192px; border-radius: 96px 0 0 96px; background: linear-gradient(100deg, #5a2a22 0%, var(--skin) 55%, #e9d6cc 100%); }
</style>
</head>
<body>
<main class="flyer">
  <svg class="backdrop" width="854" height="1200" viewBox="0 0 854 1200" aria-hidden="true">
    <defs>
      <linearGradient id="hero-tones" x1="0" y1="0" x2="1" y2="1">
        <stop offset="0" stop-color="#2a2f45"/>
        <stop offset="0.45" stop-color="#4a4f6a"/>
        <stop offset="0.8" stop-color="#a05a86"/>
        <stop offset="1" stop-color="#d27aa8"/>
      </linearGradient>
    </defs>
    <path d="M0,0 H854 V236 C680,222 470,214 300,196 C180,182 80,172 0,176 Z" fill="var(--ink-black)"/>
    <path role="img" aria-label="Model with long dark flowing hair and pink flowers, set against a soft pink bokeh backdrop" d="M0,176 C80,172 180,182 300,196 C400,206 470,214 500,240 C530,290 520,360 470,420 C410,490 280,530 0,540 Z" fill="url(#hero-tones)"/>
  </svg>

  <header class="brand">
    <span class="brand-dot"></span>
    <span class="brand-name">THE CALDER RANGE</span>
  </header>

  <h1 class="title">2017<br>PRICE<br>LIST</h1>
  <p class="offer offer-discounts">great<br>discounts</p>
  <p class="offer offer-gift">a bag gift</p>
  <p class="offer offer-loyal">for loyal customers</p>

  <section class="price-card card-high">
    <h3>high quality</h3><p class="unit">inch</p>
    <table><tr><td>12</td><td>55</td></tr><tr><td>14</td><td>62</td></tr><tr><td>16</td><td>74</td></tr><tr><td>18</td><td>81</td></tr><tr><td>20</td><td>88</td></tr><tr><td>22</td><td>97</td></tr><tr><td>24</td><td>107</td></tr><tr><td>26</td><td>112</td></tr><tr><td>28</td><td>120</td></tr><tr><td>30</td><td>128</td></tr></table>
  </section>

  <section class="price-card card-medium">
    <h3>medium quality</h3><p class="unit">inch</p>
    <table><tr><td>12</td><td>43</td></tr><tr><td>14</td><td>48</td></tr><tr><td>16</td><td>53</td></tr><tr><td>18</td><td>59</td></tr><tr><td>20</td><td>64</td></tr><tr><td>22</td><td>69</td></tr><tr><td>24</td><td>80</td></tr><tr><td>26</td><td>85</td></tr><tr><td>28</td><td>91</td></tr><tr><td>30</td><td>96</td></tr><tr><td>32</td><td>98</td></tr><tr><td>34</td><td>99</td></tr><tr><td>36</td><td>104</td></tr><tr><td>38</td><td>107</td></tr><tr><td>40</td><td>114</td></tr></table>
  </section>

  <section class="price-card card-low">
    <h3>low quality</h3><p class="unit">inch</p>
    <table><tr><td>12</td><td>29</td></tr><tr><td>14</td><td>33</td></tr><tr><td>16</td><td>39</td></tr><tr><td>18</td><td>42</td></tr><tr><td>20</td><td>46</td></tr><tr><td>22</td><td>50</td></tr><tr><td>24</td><td>54</td></tr><tr><td>26</td><td>59</td></tr><tr><td>28</td><td>65</td></tr><tr><td>30</td><td>81</td></tr></table>
  </section>

  <section class="price-card card-ombre indented">
    <h3>ombre hair<br>straight and body wave</h3><p class="unit">inch</p>
    <table><tr><td>12</td><td>50</td></tr><tr><td>14</td><td>56</td></tr><tr><td>16</td><td>67</td></tr><tr><td>18</td><td>74</td></tr><tr><td>20</td><td>80</td></tr><tr><td>22</td><td>88</td></tr><tr><td>24</td><td>98</td></tr></table>
  </section>

  <div class="photo-round" role="img" aria-label="Round photo of a model with dark curly hair"></div>
  <div class="photo-oval" role="img" aria-label="Photo of a model with glossy brown curled hair swept up"></div>

  <section class="price-card card-best-lace indented">
    <h3>best lace closure</h3><p class="unit">inch</p>
    <table><tr><td>12</td><td>64</td></tr><tr><td>14</td><td>70</td></tr><tr><td>16</td><td>78</td></tr><tr><td>18</td><td>86</td></tr><tr><td>20</td><td>92</td></tr><tr><td>22</td><td>102</td></tr><tr><td>24</td><td>104</td></tr></table>
  </section>

  <section class="price-card card-cheap-lace indented">
    <h3>cheap lace closure</h3><p class="unit">inch</p>
    <table><tr><td>10</td><td>43</td></tr><tr><td>12</td><td>48</td></tr><tr><td>14</td><td>53</td></tr><tr><td>16</td><td>58</td></tr><tr><td>18</td><td>62</td></tr><tr><td>20</td><td>66</td></tr></table>
  </section>

  <section class="price-card card-solid indented">
    <h3>solid color hair<br>straight and body wave</h3><p class="unit">inch</p>
    <table><tr><td>18</td><td>63</td></tr><tr><td>20</td><td>72</td></tr><tr><td>22</td><td>83</td></tr><tr><td>24</td><td>90</td></tr></table>
  </section>

  <section class="price-card card-deep indented">
    <h3>deep wave</h3><p class="unit">inch</p>
    <table><tr><td>18</td><td>66</td></tr><tr><td>20</td><td>75</td></tr><tr><td>22</td><td>86</td></tr><tr><td>24</td><td>94</td></tr></table>
  </section>
</main>
</body>
</html>
```